Redesign, cleanup and edit my Presentations

I have a series of power points that I use for training purposes. They were made by me over time. During the last couple years, I have evolved their look and content over time, but not consistently. More specifically, I have not gone back to re-edit the older decks. So, some decks are too wordy, too long, or and don't look consistent.

I am looking someone who can create a good design that I can use going forward, and who could also apply that theme to the existing decks, along with editing the existing, and future decks, too.

I have a lot of slides to produce and/or edit -approximately 500. But this request is a test to find a powerpoint partner. I am supplying 2 decks. One that's older and more wordy than the other. I would like to see what you would suggest we do differently. So that's what you are bidding on today. Also, you do not have to complete deck "Phase 7.4." I only need enough of the deck done to see where you would take it. Maybe 10 slides? Your choice. However, with that deck, there are lots of opportunities to clarify, re-align, and minimize within that deck.

But, if you are selected, I want to engage with you on an ongoing basis, and send more material your way. Then, you will be engaged to complete all decks.

Please ask me any questions to help you gain a better understanding of this project.

Target Market(s)

People in management, technical, medical, and financial fields who wish to become independent consultants.

Industry/Entity Type

Business Consultant

Font styles to use
Sans Serif

Requirements
Must have
• Use the existing color theme:
• yellow/gold - #f5b300,
• blue - 2b74a6
• Logo doesn't change
• Preferred fonts: Raleway for headings and Open Sans for general text
• Any pictures and graphics should have no copyright restrictions. That is, I should have use of the work without charge.
Nice to have
• I prefer a flat graphic style, although you can use pictures where it conveys a point more effectively.
• Ability to convert the presentations to Google Slides and Apple's Keynote apps.
• Ability to convert presentation to video
Should not have
• Restricted use graphics, photos, or other content.

```html
<!DOCTYPE html>
<html lang="en">
<head>
<meta charset="utf-8">
<title>Corvane – Presentation Theme Overview</title>
<link href="https://fonts.googleapis.com/css2?family=Open+Sans:wght@400;600;700&family=Raleway:wght@500;600&display=swap" rel="stylesheet">
<style>
:root{
  --page:#4b5961;
  --blue:#1c5e9e;
  --blue-deep:#17508a;
  --teal:#1787b5;
  --sky:#a9cdec;
  --sky-soft:#d6e7f6;
  --gold:#f5b300;
  --ink:#3b4650;
  --grey-box:#e9ebed;
  --white:#ffffff;
}
*{box-sizing:border-box;margin:0;padding:0}
html,body{width:1200px;height:1200px;overflow:hidden;background:var(--page)}
body{position:relative;font-family:"Open Sans",Arial,sans-serif;color:var(--ink)}
.slide{position:absolute;width:363px;height:204px;overflow:hidden;background:var(--white)}
.slide.is-blue{background:var(--blue);color:var(--white)}
.abs{position:absolute}
.photo{position:absolute;background:linear-gradient(135deg,#8d98a3,#cfd5da 55%,#6f7b86)}
.brand{position:absolute;display:flex;align-items:center;gap:3px;font-family:"Open Sans",sans-serif;font-weight:600;color:var(--blue);white-space:nowrap;letter-spacing:.2px}
.brand-dot{display:inline-block;border-radius:50%;background:var(--gold)}
.is-blue .brand,.brand.on-dark{color:var(--white)}
.slide-title{position:absolute;left:17px;top:14px;font-family:"Raleway",sans-serif;font-weight:500;font-size:13px;color:var(--blue)}
.kicker-dots{position:absolute;left:17px;top:8px;font-size:6px;letter-spacing:2px;color:var(--sky);line-height:1}
.tiny{font-size:4.4px;line-height:1.35}
.small{font-size:5.2px;line-height:1.35}
.label{font-size:5.4px;color:var(--blue);font-weight:600}
.foot{position:absolute;left:10px;right:10px;bottom:6px;height:12px;display:flex;align-items:center;gap:6px;font-size:3.8px;color:#9aa4ad}
.foot .brand{position:static;font-size:9px}
.foot .brand-dot{width:7px;height:7px}
.foot .sep{width:.5px;height:7px;background:#c5ccd2}
.foot .pager{margin-left:auto;display:flex;gap:5px}
.foot .pager i{width:2px;height:2px;border-radius:50%;background:var(--sky)}
.foot .pager i:last-child{background:var(--teal)}
.corner-arc{position:absolute;right:-40px;bottom:-62px;width:110px;height:110px;border-radius:50%;border:9px solid var(--sky-soft)}
.title-lg{font-family:"Raleway",sans-serif;font-weight:500;line-height:1.12}
</style>
</head>
<body>

<!-- Row 1 -->
<section class="slide cover-light" style="left:47px;top:58px">
  <div class="abs" style="left:150px;top:-18px;width:220px;height:220px;border-radius:50%;background:var(--sky-soft)"></div>
  <div class="abs" style="left:318px;top:24px;width:8px;height:52px;background:var(--sky)"></div>
  <div class="abs" style="left:192px;top:140px;width:18px;height:70px;background:#f8d27a"></div>
  <div class="photo" role="img" aria-label="Photo: team meeting around a table seen from above" style="left:171px;top:18px;width:148px;height:148px;border-radius:50%"></div>
  <div class="brand" style="left:19px;top:22px;font-size:16px"><i class="brand-dot" style="width:13px;height:13px"></i>Corvane</div>
  <p class="abs tiny" style="left:19px;top:60px">Corvane presents:</p>
  <h1 class="abs title-lg" style="left:19px;top:70px;font-size:15.5px;color:var(--blue)">The Strategy<br>of Mastering<br>your Pitch</h1>
  <p class="abs tiny" style="left:19px;top:164px">July 2019<br>prepared by: Author's Name</p>
  <p class="abs tiny" style="left:19px;top:186px">www.corvane-example.com</p>
</section>

<section class="slide is-blue cover-blue" style="left:422px;top:58px">
  <div class="abs" style="left:176px;top:38px;width:40px;height:70px;background:var(--blue-deep)"></div>
  <div class="abs" style="left:318px;top:38px;width:7px;height:40px;background:var(--sky)"></div>
  <div class="photo" role="img" aria-label="Photo: team meeting around a table seen from above" style="left:178px;top:16px;width:148px;height:148px;border-radius:50%"></div>
  <div class="brand" style="left:21px;top:22px;font-size:16px"><i class="brand-dot" style="width:13px;height:13px"></i>Corvane</div>
  <p class="abs tiny" style="left:21px;top:68px">Corvane presents:</p>
  <h1 class="abs title-lg" style="left:21px;top:78px;font-size:15.5px">The Strategy<br>of Mastering<br>your Pitch</h1>
  <p class="abs tiny" style="left:21px;top:162px">July 2019<br>prepared by: Author's Name</p>
  <p class="abs tiny" style="left:21px;top:182px">www.corvane-example.com</p>
  <div class="abs" style="left:21px;top:193px;width:290px;height:.5px;background:#5b8cc0"></div>
  <p class="abs" style="left:328px;top:186px;font-size:7px;letter-spacing:1px">•••</p>
</section>

<section class="slide cover-photo" style="left:797px;top:58px">
  <div class="photo" role="img" aria-label="Photo: light trails on a mountain road at dusk, tinted blue" style="inset:0;width:auto;height:auto;background:linear-gradient(160deg,#1d4f8f,#2e6db0 45%,#1a4a86 70%,#2a6aa8)"></div>
  <div class="abs" style="left:90px;top:-30px;width:180px;height:180px;border-radius:50%;background:rgba(255,255,255,.07)"></div>
  <div class="brand on-dark" style="left:0;right:0;top:34px;justify-content:center;font-size:17px"><i class="brand-dot" style="width:14px;height:14px"></i>Corvane</div>
  <h1 class="abs title-lg" style="left:0;right:0;top:78px;text-align:center;font-size:15.5px;color:#fff">The Strategy of<br>Mastering your Pitch</h1>
  <p class="abs small" style="left:0;right:0;top:152px;text-align:center;color:#fff">July 2019<br>prepared by: Author's Name</p>
  <p class="abs small" style="left:0;right:0;top:182px;text-align:center;color:var(--gold)">www.corvane-example.com</p>
</section>

<!-- Row 2 -->
<section class="slide is-blue agenda" style="left:47px;top:278px">
  <div class="brand" style="right:22px;top:22px;font-size:14px"><i class="brand-dot" style="width:11px;height:11px"></i>Corvane</div>
  <h2 class="abs title-lg" style="left:29px;top:38px;font-size:12.5px">Agenda</h2>
  <p class="abs" style="left:29px;top:54px;font-size:6px;letter-spacing:1.5px;color:var(--sky)">•••</p>
  <ol class="abs" style="left:29px;top:77px;width:150px;list-style:none">
    <li style="display:flex;gap:6px;margin-bottom:6px"><span class="small">1</span><div><p class="small">Introduction</p><p class="tiny" style="color:#c8dbef">Short line on what this part covers<br>and why it matters here</p></div></li>
    <li style="display:flex;gap:6px;margin-bottom:6px"><span class="small">2</span><div><p class="small">The Company</p><p class="tiny" style="color:#c8dbef">Who we are and how we work<br>with our clients each day</p></div></li>
    <li style="display:flex;gap:6px;margin-bottom:6px"><span class="small">3</span><div><p class="small">The Business Value</p><p class="tiny" style="color:#c8dbef">What changes for your team<br>after the program</p></div></li>
    <li style="display:flex;gap:6px"><span class="small">4</span><div><p class="small">The Private Equity</p><p class="tiny" style="color:#c8dbef">How investors read results<br>in the first year</p></div></li>
  </ol>
  <ol class="abs" style="left:192px;top:77px;width:160px;list-style:none">
    <li style="display:flex;gap:6px;margin-bottom:6px"><span class="small">5</span><div><p class="small">Why Choose Us</p><p class="tiny" style="color:#c8dbef">Clear reasons backed by proven<br>outcomes and experience</p></div></li>
    <li style="display:flex;gap:6px;margin-bottom:6px"><span class="small">6</span><div><p class="small">Our Clients</p><p class="tiny" style="color:#c8dbef">Teams we have supported across<br>many different sectors</p></div></li>
    <li style="display:flex;gap:6px;margin-bottom:6px"><span class="small">7</span><div><p class="small">Lorem Ipsum</p><p class="tiny" style="color:#c8dbef">Placeholder section for extra<br>content when it is needed</p></div></li>
    <li style="display:flex;gap:6px"><span class="small">8</span><div><p class="small">Contact Us</p><p class="tiny" style="color:#c8dbef">Where to reach us next</p></div></li>
  </ol>
</section>

<section class="slide is-blue divider" style="left:422px;top:278px">
  <svg class="abs" style="left:70px;top:-2px" width="230" height="210" viewBox="0 0 230 210" aria-hidden="true">
    <circle cx="115" cy="105" r="102" fill="none" stroke="#2a6cae" stroke-width="1"/>
    <path d="M40 30 A102 102 0 0 1 200 40" fill="none" stroke="var(--gold)" stroke-width="1"/>
    <path d="M215 120 A102 102 0 0 1 170 190" fill="none" stroke="var(--gold)" stroke-width="1"/>
  </svg>
  <div class="photo" role="img" aria-label="Photo: people in an office meeting, blue tint" style="left:91px;top:8px;width:190px;height:190px;border-radius:50%;background:radial-gradient(circle at 50% 40%,#5b86b8,#3d6ea6 70%)"></div>
  <svg class="abs" style="left:173px;top:66px" width="24" height="20" viewBox="0 0 24 20" aria-hidden="true" fill="none" stroke="#fff" stroke-width="1">
    <circle cx="14" cy="8" r="6"/><path d="M8 8h12M14 2v12M10 3.5c2 3 2 6 0 9M18 3.5c-2 3-2 6 0 9"/><circle cx="5" cy="12" r="2.5"/><path d="M1 19c0-3 2-4.5 4-4.5s4 1.5 4 4.5"/>
  </svg>
  <h2 class="abs title-lg" style="left:0;right:0;top:102px;text-align:center;font-size:14.5px">divider title</h2>
  <p class="abs tiny" style="left:0;right:0;top:122px;text-align:center;font-size:5px;color:#d6e4f3">place a subtitle / desc here</p>
  <div class="brand" style="left:0;right:0;top:138px;justify-content:center;font-size:14px"><i class="brand-dot" style="width:11px;height:11px"></i>Corvane</div>
</section>

<section class="slide company" style="left:797px;top:278px">
  <p class="kicker-dots">•••</p>
  <h2 class="slide-title">The Company</h2>
  <div class="photo" role="img" aria-label="Photo: people talking in a bright office lobby" style="left:17px;top:40px;width:198px;height:49px"></div>
  <div class="photo" role="img" aria-label="Photo: office scene with blue tint" style="left:215px;top:40px;width:148px;height:49px;background:linear-gradient(135deg,#8fb5de,#c3d8ee)"></div>
  <p class="abs label" style="left:17px;top:96px;color:var(--ink);font-weight:400">About Corvane</p>
  <p class="abs tiny" style="left:17px;top:106px;width:190px;color:#7a858f">Corvane is a leadership development consultancy that helps leaders and their organizations grow. We blend coaching, training and technology into one program that fits how modern teams work today.</p>
  <p class="abs label" style="left:213px;top:96px;font-weight:400">The Difference</p>
  <p class="abs tiny" style="left:213px;top:106px;width:135px;color:#7a858f">We set the standard in modern leadership coaching and team growth. Our programs combine business insight with proven methods to drive lasting change. When you want to lift your leaders, we are the partner that brings people, process and the right platform together to make it happen.</p>
  <div class="foot"><span class="brand"><i class="brand-dot"></i>Corvane</span><span>Document title goes here on the bottom right</span><i class="sep"></i><span>www.corvane-example.com</span><span class="pager"><i></i><i></i><i></i></span></div>
</section>

<!-- Row 3 -->
<section class="slide timeline-icons" style="left:47px;top:498px">
  <p class="kicker-dots">•••</p>
  <h2 class="slide-title">Timeline</h2>
  <div class="corner-arc"></div>
  <svg class="abs" style="left:0;top:0" width="363" height="204" viewBox="0 0 363 204" aria-hidden="true" fill="none" stroke="var(--blue)" stroke-width=".8">
    <g stroke-dasharray="2 2" stroke="var(--teal)">
      <path d="M68 106h14M126 106h14M184 106h14M242 106h14M300 106h14"/>
      <path d="M49 86V72M165 86V72M281 86V72M107 126v22M223 126v22M339 126v22"/>
    </g>
    <g stroke="var(--teal)">
      <circle cx="49" cy="106" r="19"/><circle cx="107" cy="106" r="19"/><circle cx="165" cy="106" r="19"/>
      <circle cx="223" cy="106" r="19"/><circle cx="281" cy="106" r="19"/>
    </g>
    <circle cx="339" cy="106" r="19" fill="var(--blue)" stroke="none"/>
    <path d="M332 106l5 5 9-10" stroke="#fff" stroke-width="1.6" stroke-linecap="round" stroke-linejoin="round"/>
    <g stroke="var(--blue)">
      <circle cx="44" cy="101" r="3"/><circle cx="54" cy="101" r="3"/><path d="M38 113c0-5 3-7 6-7s6 2 6 7M48 113c0-5 3-7 6-7s6 2 6 7"/>
      <path d="M100 99l14 14M114 99l-14 14M100 99h4M100 99v4M114 113h-4M114 113v-4"/>
      <path d="M157 114h16M158 112v-4M162 112v-7M166 112v-5M170 112v-9M157 106l5-4 4 2 6-6"/>
      <path d="M214 104l6-5 5 3 6-4M214 104l7 7 3-2M231 98l2 6-7 7"/>
      <rect x="275" y="97" width="12" height="18"/><path d="M278 101h2M283 101h2M278 105h2M283 105h2M278 109h2M283 109h2"/>
    </g>
  </svg>
  <div class="abs tiny" style="left:32px;top:38px;width:80px"><p style="color:var(--ink);margin-bottom:2px">2012</p><p>Short note on a key moment that shaped the way we work</p></div>
  <div class="abs tiny" style="left:148px;top:38px;width:80px"><p style="margin-bottom:2px">2014</p><p>Short note on a key moment that shaped the way we work</p></div>
  <div class="abs tiny" style="left:264px;top:38px;width:80px"><p style="margin-bottom:2px">2016</p><p>Short note on a key moment that shaped the way we work</p></div>
  <div class="abs tiny" style="left:22px;top:141px;width:80px;text-align:right"><p style="margin-bottom:2px">2013</p><p>Short note on a key moment that shaped the way we work</p></div>
  <div class="abs tiny" style="left:138px;top:141px;width:80px;text-align:right"><p style="margin-bottom:2px">2017</p><p>Short note on a key moment that shaped the way we work</p></div>
  <div class="abs tiny" style="left:254px;top:141px;width:80px;text-align:right"><p style="margin-bottom:2px">2019</p><p>Short note on a key moment that shaped the way we work</p></div>
  <div class="foot"><span class="brand"><i class="brand-dot"></i>Corvane</span><span>Document title goes here on the bottom right</span><i class="sep"></i><span>www.corvane-example.com</span><span class="pager"><i></i><i></i><i></i></span></div>
</section>

<section class="slide step-profile" style="left:422px;top:498px">
  <div class="photo" role="img" aria-label="Photo: colleagues talking in a lounge" style="left:0;top:0;width:168px;height:180px"></div>
  <div class="abs" style="left:168px;top:0;width:185px;height:180px;background:var(--blue);color:#fff;padding:15px 10px 0 13px">
    <p class="tiny" style="font-size:5px">STEP 1</p>
    <h2 class="title-lg" style="font-size:11.5px;margin-top:1px">Build A Background Profile</h2>
    <p style="font-size:5px;letter-spacing:1.2px;color:var(--sky);margin:3px 0">•••</p>
    <p class="small" style="margin-bottom:6px">Background, or demographics, is basic information the profile starts from.</p>
    <p class="tiny" style="margin-bottom:5px">For B2C profiles this can include age, gender, marital status, location, education, income or any other detail that helps you empathize with your target.</p>
    <p class="tiny" style="margin-bottom:5px">Thanks to your market research in Step 2, and your keyword research, you already hold a lot of this information. If you don't, start by talking to clients and noting what they share.</p>
    <p class="tiny">Be specific enough that you can picture the person, but keep it open enough to stay useful.</p>
  </div>
  <div class="foot" style="left:10px"><span class="brand"><i class="brand-dot"></i>Corvane</span><span>Document title goes here on the bottom right</span><i class="sep"></i><span>www.corvane-example.com</span><span class="pager"><i></i><i></i><i></i></span></div>
</section>

<section class="slide timeline-chart" style="left:797px;top:498px">
  <p class="kicker-dots">•••</p>
  <h2 class="slide-title">Timeline</h2>
  <div class="corner-arc"></div>
  <p class="abs small" style="left:23px;top:46px;width:90px;font-size:4.6px">Lorem ipsum is dummy text that can be replaced with your own text for this section.</p>
  <p class="abs tiny" style="left:23px;top:82px;width:88px;color:#7a858f">Add a short summary of what the chart shows and why the trend matters to the audience. Keep it to a few lines so the data stays the focus of the slide.</p>
  <svg class="abs" style="left:118px;top:44px" width="236" height="130" viewBox="0 0 236 130" aria-label="Area chart of two categories from 2017 to 2023" role="img">
    <g font-size="4.4" fill="#7a858f" font-family="Open Sans, sans-serif">
      <text x="6" y="6">60</text><text x="6" y="23">50</text><text x="6" y="40">40</text><text x="6" y="57">30</text><text x="6" y="74">20</text><text x="6" y="91">10</text><text x="9" y="107">0</text>
      <g text-anchor="middle"><text x="24" y="115">2017</text><text x="56" y="115">2018</text><text x="91" y="115">2019</text><text x="126" y="115">2020</text><text x="161" y="115">2021</text><text x="196" y="115">2022</text></g>
      <text x="234" y="115" text-anchor="end">2023</text>
    </g>
    <path d="M22 105 V45 L56 59 L91 38 L126 45 L161 30 L196 25 L232 20 V105Z" fill="var(--gold)"/>
    <path d="M22 105 V78 L56 70 L91 72 L126 58 L161 62 L196 56 L232 37 V105Z" fill="var(--teal)"/>
    <rect x="22" y="122" width="5" height="5" fill="var(--gold)"/><text x="30" y="126.5" font-size="4.4" fill="#7a858f" font-family="Open Sans, sans-serif">Category Name</text>
    <rect x="86" y="122" width="5" height="5" fill="var(--teal)"/><text x="94" y="126.5" font-size="4.4" fill="#7a858f" font-family="Open Sans, sans-serif">Category Name</text>
  </svg>
  <div class="foot"><span class="brand"><i class="brand-dot"></i>Corvane</span><span>Document title goes here on the bottom right</span><i class="sep"></i><span>www.corvane-example.com</span><span class="pager"><i></i><i></i><i></i></span></div>
</section>

<!-- Row 4 -->
<section class="slide our-value" style="left:47px;top:721px">
  <p class="kicker-dots">•••</p>
  <h2 class="slide-title">Our Value</h2>
  <div class="corner-arc"></div>
  <div class="abs" style="left:18px;top:37px;width:157px;height:25px;background:var(--grey-box)"></div>
  <div class="abs" style="left:185px;top:37px;width:157px;height:25px;background:var(--grey-box)"></div>
  <p class="abs label" style="left:18px;top:65px;font-weight:400;font-size:4.6px">Results</p>
  <p class="abs tiny" style="left:18px;top:72px;width:157px;color:#7a858f">From the first meeting to the final handshake, our aim is to bring real change to people and their teams. We identify, track and measure what matters so every result is captured in a clear success story.</p>
  <p class="abs label" style="left:185px;top:65px;font-weight:400;font-size:4.6px">Integrity</p>
  <p class="abs tiny" style="left:185px;top:72px;width:157px;color:#7a858f">Trust and partnership are at the core of our work. We choose our coaches with care, based on skill and the values we promote.</p>
  <div class="abs" style="left:18px;top:110px;width:157px;height:25px;background:var(--grey-box)"></div>
  <div class="abs" style="left:185px;top:110px;width:157px;height:25px;background:var(--grey-box)"></div>
  <p class="abs label" style="left:18px;top:138px;font-weight:400;font-size:4.6px">Innovation</p>
  <p class="abs tiny" style="left:18px;top:145px;width:157px;color:#7a858f">We keep refining our methods to meet the changing needs of our clients, whether that means new tools or a fresh approach to coaching.</p>
  <p class="abs label" style="left:185px;top:138px;font-weight:400;font-size:4.6px">Science</p>
  <p class="abs tiny" style="left:185px;top:145px;width:150px;color:#7a858f">In a crowded coaching field we rely on evidence. Our services are built on sound principles of learning, motivation and behavior.</p>
  <div class="foot"><span class="brand"><i class="brand-dot"></i>Corvane</span><span>Document title goes here on the bottom right</span><i class="sep"></i><span>www.corvane-example.com</span><span class="pager"><i></i><i></i><i></i></span></div>
</section>

<section class="slide big-image" style="left:422px;top:721px">
  <div class="abs" style="left:0;top:0;width:178px;height:180px;background:var(--blue);color:#fff;padding:14px 10px 0 17px">
    <p class="tiny" style="font-size:4.8px">SUB TITLE</p>
    <h2 class="title-lg" style="font-size:11.5px;margin-top:1px">Big Image with Text</h2>
    <p style="font-size:5px;letter-spacing:1.2px;color:var(--sky);margin:3px 0 5px">•••</p>
    <p class="small" style="font-size:5.6px;margin-bottom:6px">Add one short key message here.<br>Support it with a second clear line<br>that leads into the detail below.</p>
    <p class="tiny" style="color:#d6e4f3">Use this space for the body copy of the slide. Keep paragraphs short and focused so the image can carry part of the message. Explain the idea, give one example, and close with the takeaway you want the audience to remember after the session ends.</p>
  </div>
  <div class="photo" role="img" aria-label="Photo: modern glass roof structure in blue tones" style="left:178px;top:0;width:175px;height:180px;background:linear-gradient(140deg,#0e3f6b,#3d8fc4 45%,#bfe0f2 60%,#1b5d92)"></div>
  <div class="foot"><span class="brand"><i class="brand-dot"></i>Corvane</span><span>Document title goes here on the bottom right</span><i class="sep"></i><span>www.corvane-example.com</span><span class="pager"><i></i><i></i><i></i></span></div>
</section>

<section class="slide what-we-do" style="left:797px;top:721px">
  <p class="kicker-dots">•••</p>
  <h2 class="slide-title">What We Do</h2>
  <div class="corner-arc"></div>
  <div class="abs" style="left:22px;top:39px;width:341px;display:grid;grid-template-columns:repeat(3,102px);gap:7px 8px">
    <article style="height:68px;background:var(--teal);color:#fff;padding:5px 6px"><p style="font-size:4px;opacity:.7">▦</p><p class="small" style="margin:1px 0 2px">Executive Coaching</p><p class="tiny" style="font-size:3.8px">Coaching built around the growth of one leader, using a clear four step process for lasting change.</p></article>
    <article style="height:68px;background:var(--gold);color:#fff;padding:5px 6px"><p style="font-size:4px;opacity:.7">▦</p><p class="small" style="margin:1px 0 2px">Leadership Development</p><p class="tiny" style="font-size:3.8px">Leadership is a skill that can be learned. We help leaders practise it and keep it growing.</p></article>
    <article style="height:68px;background:var(--teal);color:#fff;padding:5px 6px"><p style="font-size:4px;opacity:.7">▦</p><p class="small" style="margin:1px 0 2px">Team Effectiveness</p><p class="tiny" style="font-size:3.8px">A team coaching program for groups that want high performance that lasts.</p></article>
    <article style="height:68px;background:var(--gold);color:#fff;padding:5px 6px"><p style="font-size:4px;opacity:.7">▦</p><p class="small" style="margin:1px 0 2px">Organizational Effectiveness</p><p class="tiny" style="font-size:3.8px">Coaching aimed at the whole organization, with a clear process for steady change.</p></article>
    <article style="height:68px;background:var(--teal);color:#fff;padding:5px 6px"><p style="font-size:4px;opacity:.7">▦</p><p class="small" style="margin:1px 0 2px">Coaching Skills for Leaders</p><p class="tiny" style="font-size:3.8px">Coaching is now a core leadership skill. We teach it so managers can lift their own teams.</p></article>
    <article style="height:68px;background:var(--gold);color:#fff;padding:5px 6px"><p style="font-size:4px;opacity:.7">▦</p><p class="small" style="margin:1px 0 2px">Coaching Technology</p><p class="tiny" style="font-size:3.8px">A platform to run and track coaching programs, with a simple dashboard for results.</p></article>
  </div>
  <div class="foot"><span class="brand"><i class="brand-dot"></i>Corvane</span><span>Document title goes here on the bottom right</span><i class="sep"></i><span>www.corvane-example.com</span><span class="pager"><i></i><i></i><i></i></span></div>
</section>

<!-- Row 5 -->
<section class="slide testimonial" style="left:47px;top:944px">
  <p class="kicker-dots">•••</p>
  <h2 class="slide-title">Testimonial</h2>
  <div class="corner-arc"></div>
  <p class="abs tiny" style="left:19px;top:40px;width:320px;font-size:4.7px">Use this line to introduce what clients say about working with us, and why their words matter for the decision in front of you.</p>
  <div class="abs" style="left:26px;top:61px;width:308px;height:54px;background:var(--gold)">
    <div class="photo" role="img" aria-label="Portrait photo of a client" style="left:20px;top:7px;width:40px;height:40px"></div>
    <p class="abs" style="left:68px;top:8px;font-size:12px;line-height:1;color:var(--ink);font-weight:700">“</p>
    <p class="abs" style="left:84px;top:11px;width:210px;font-size:8.2px;line-height:1.3;color:var(--ink)">Make quote really big so people can read them. It can be your brand endorsement.</p>
    <p class="abs tiny" style="left:84px;top:38px;color:var(--ink)">- Daniel Brooks - Owner of Harbor Point Group</p>
    <p class="abs" style="left:276px;top:30px;font-size:12px;line-height:1;color:var(--ink);font-weight:700">”</p>
  </div>
  <div class="abs" style="left:26px;top:126px;width:308px;height:54px;background:var(--teal);color:#fff">
    <p class="abs" style="left:26px;top:8px;font-size:12px;line-height:1;font-weight:700">“</p>
    <p class="abs" style="left:40px;top:11px;width:210px;font-size:8.2px;line-height:1.3">Make quote really big so people can read them. It can be your brand endorsement.</p>
    <p class="abs tiny" style="left:40px;top:38px">- Maya Ellison - Owner of Harbor Point Group</p>
    <p class="abs" style="left:231px;top:30px;font-size:12px;line-height:1;font-weight:700">”</p>
    <div class="photo" role="img" aria-label="Portrait photo of a client" style="left:259px;top:7px;width:40px;height:40px"></div>
  </div>
  <div class="foot"><span class="brand"><i class="brand-dot"></i>Corvane</span><span>Document title goes here on the bottom right</span><i class="sep"></i><span>www.corvane-example.com</span><span class="pager"><i></i><i></i><i></i></span></div>
</section>

<section class="slide case-study" style="left:422px;top:944px">
  <div class="abs" style="left:0;top:0;width:142px;height:204px;background:var(--blue)"></div>
  <p class="abs" style="left:11px;top:6px;font-size:6px;letter-spacing:1.5px;color:var(--sky)">•••</p>
  <h2 class="abs title-lg" style="left:18px;top:17px;font-size:13px;color:#fff">Case Study</h2>
  <div class="photo" role="img" aria-label="Photo: hands working on a laptop and paper charts" style="left:19px;top:40px;width:200px;height:118px"></div>
  <div class="abs tiny" style="left:228px;top:40px;width:112px">
    <p style="font-size:5px;color:var(--ink)">Outline Brief</p>
    <p style="color:#7a858f;margin-bottom:4px">Short summary of the client, the challenge and the goal.</p>
    <div style="height:.5px;background:var(--teal);margin-bottom:5px"></div>
    <p style="font-size:5px;color:var(--ink)">Methodology</p>
    <p style="color:#7a858f;margin-bottom:4px">The steps we took, the tools we used and how we worked with the team.</p>
    <div style="height:.5px;background:var(--teal);margin-bottom:5px"></div>
    <p style="font-size:5px;color:var(--ink)">Review</p>
    <p style="color:#7a858f">What changed, with one clear result to close the story.</p>
  </div>
  <div class="abs" style="right:-40px;bottom:-62px;width:110px;height:110px;border-radius:50%;border:9px solid var(--sky-soft)"></div>
  <div class="foot"><span class="brand" style="color:#fff"><i class="brand-dot"></i>Corvane</span><span style="margin-left:auto">Document title goes here on the bottom right</span><i class="sep"></i><span>www.corvane-example.com</span><span class="pager" style="margin-left:0"><i></i><i></i><i></i></span></div>
</section>

<section class="slide case-details" style="left:797px;top:944px">
  <div class="photo" role="img" aria-label="Photo: team meeting seen from above" style="left:0;top:0;width:82px;height:204px"></div>
  <div class="abs" style="left:82px;top:0;width:82px;height:204px;background:var(--blue)"></div>
  <svg class="abs" style="left:108px;top:20px" width="30" height="160" viewBox="0 0 30 160" aria-hidden="true" fill="none" stroke="#fff" stroke-width=".8">
    <path d="M15 26v8M15 74v8M15 122v8" stroke="#6f9bcc"/>
    <circle cx="15" cy="14" r="11"/><circle cx="15" cy="46" r="11"/><circle cx="15" cy="94" r="11"/><circle cx="15" cy="142" r="11"/>
  </svg>
  <p class="kicker-dots" style="left:176px">•••</p>
  <h2 class="slide-title" style="left:183px;font-size:12px">Case Study Details</h2>
  <p class="abs small" style="left:183px;top:38px;width:160px;font-size:4.8px">Lorem ipsum is dummy text that can be replaced with your own text.</p>
  <p class="abs tiny" style="left:183px;top:52px;width:160px;color:#7a858f">Add a short line that sets up the four variables shown below for this case.</p>
  <div class="abs tiny" style="left:183px;top:92px;width:75px"><p style="font-size:4.8px">Variable A</p><div style="height:.5px;background:var(--teal);margin:1px 0 2px"></div><p style="color:#7a858f">One short note on this variable and its result.</p></div>
  <div class="abs tiny" style="left:268px;top:92px;width:75px"><p style="font-size:4.8px">Variable B</p><div style="height:.5px;background:var(--teal);margin:1px 0 2px"></div><p style="color:#7a858f">One short note on this variable and its result.</p></div>
  <div class="abs tiny" style="left:183px;top:147px;width:75px"><p style="font-size:4.8px">Variable C</p><div style="height:.5px;background:var(--teal);margin:1px 0 2px"></div><p style="color:#7a858f">One short note on this variable and its result.</p></div>
  <div class="abs tiny" style="left:268px;top:147px;width:75px"><p style="font-size:4.8px">Variable D</p><div style="height:.5px;background:var(--teal);margin:1px 0 2px"></div><p style="color:#7a858f">One short note on this variable and its result.</p></div>
  <div class="foot"><span class="brand" style="color:#fff"><i class="brand-dot"></i>Corvane</span><span style="margin-left:auto">Document title goes here on the bottom right</span><i class="sep"></i><span>www.corvane-example.com</span><span class="pager" style="margin-left:0"><i></i><i></i><i></i></span></div>
</section>

</body>
</html>
```